New Business Card Needed

I need a new business card for Willowmere Kitchen & Bath.
Logo is attached as well a my photo. Note: Make the logo Navy Blue.
Here is the text:
Desmond Ferrick
GC/Owner
Charlotte NC
704-555-0183
desmond@willowmereKB.example
www.willowmereKB.example
Tag line on card: BEAUTY | FUNCTION | ON TIME | ON BUDGET
Trim size: 2.56" X 2.56"
This is where we aim to cut the cards.
Safe area: 2.4" X 2.4"
Make sure any important aspects of your design such as text and logos are inside of the safe area, otherwise they may be cut off.
Bleed area: 2.71 X 2.71
Make sure that your background extends to fill the bleed to avoid your Business Cards having white edges when trimmed.
On the back side. Use photo of kitchen attached.

```html
<!DOCTYPE html>
<html lang="en">
<head>
<meta charset="utf-8">
<title>Willowmere Kitchen &amp; Bath – Business Card</title>
<link href="https://fonts.googleapis.com/css2?family=Lato:wght@400;700;900&display=swap" rel="stylesheet">
<style>
  :root {
    --navy: #0f1f4b;
    --white: #ffffff;
    --stage: #3a3a3c;
    --ink-soft: #1c2540;
    --wood: #c9a878;
    --stone: #ebe8e4;
    --floor: #9a6a45;
  }
  html, body {
    margin: 0;
    width: 1200px;
    height: 694px;
    overflow: hidden;
    background: var(--stage);
    font-family: "Lato", sans-serif;
  }
  .sheet {
    position: relative;
    width: 1200px;
    height: 694px;
  }
  .card {
    position: absolute;
    top: 187px;
    width: 560px;
    height: 320px;
    overflow: hidden;
    box-shadow: 0 10px 30px rgba(0,0,0,.45);
  }
  .card--back { left: 25px; }
  .card--front { left: 615px; background: var(--white); }

  .kitchen-photo {
    width: 100%;
    height: 100%;
    background:
      linear-gradient(180deg, var(--stone) 0%, #e3dcd2 35%, var(--wood) 55%, #d8d2ca 70%, var(--floor) 100%);
  }

  .brand {
    position: absolute;
    left: 34px;
    top: 44px;
    display: flex;
    align-items: center;
    gap: 10px;
    color: var(--navy);
    font-weight: 700;
    font-size: 21px;
    line-height: 1.05;
    letter-spacing: .5px;
  }
  .brand__mark {
    width: 16px;
    height: 16px;
    background: var(--navy);
    flex: none;
  }

  .contact {
    position: absolute;
    left: 34px;
    top: 112px;
    color: var(--ink-soft);
  }
  .contact__name {
    margin: 0;
    font-weight: 900;
    font-size: 24px;
    color: var(--navy);
  }
  .contact__role {
    margin: 2px 0 12px;
    font-size: 15px;
  }
  .contact__list {
    list-style: none;
    margin: 0;
    padding: 0;
    font-size: 13.5px;
  }
  .contact__list li {
    display: flex;
    align-items: center;
    gap: 9px;
    height: 23px;
  }
  .contact__list svg { width: 15px; height: 15px; flex: none; fill: var(--navy); }
  .contact__city { margin-top: 8px; font-size: 14px; }

  .portrait {
    position: absolute;
    right: 22px;
    top: 22px;
    width: 230px;
    height: 250px;
    background: linear-gradient(180deg, #efe9e5 0%, #d9c3b4 45%, #3b4766 80%, #2a3455 100%);
    border-radius: 4px 4px 0 0;
  }

  .tagline {
    position: absolute;
    left: 0;
    right: 0;
    bottom: 0;
    height: 48px;
    background: var(--navy);
    color: var(--white);
    display: flex;
    align-items: center;
    justify-content: flex-end;
    padding-right: 22px;
    font-weight: 700;
    font-size: 17px;
    letter-spacing: .4px;
  }
</style>
</head>
<body>
<main class="sheet">
  <section class="card card--back">
    <div class="kitchen-photo" role="img" aria-label="Photo of a bright remodeled kitchen with light wood cabinets, white subway tile, marble island and bar stools"></div>
  </section>

  <section class="card card--front">
    <div class="brand">
      <span class="brand__mark"></span>
      <span>Willowmere<br>Kitchen &amp; Bath</span>
    </div>

    <div class="contact">
      <h1 class="contact__name">Desmond Ferrick</h1>
      <p class="contact__role">GC/Owner</p>
      <ul class="contact__list">
        <li>
          <svg viewBox="0 0 24 24" aria-hidden="true"><path d="M6.6 10.8a15.1 15.1 0 0 0 6.6 6.6l2.2-2.2a1 1 0 0 1 1-.25 11.4 11.4 0 0 0 3.6.57 1 1 0 0 1 1 1V20a1 1 0 0 1-1 1A17 17 0 0 1 3 4a1 1 0 0 1 1-1h3.5a1 1 0 0 1 1 1c0 1.25.2 2.45.57 3.57a1 1 0 0 1-.25 1z"/></svg>
          704-555-0183
        </li>
        <li>
          <svg viewBox="0 0 24 24" aria-hidden="true"><path d="M2 5h20v14H2z M2 5l10 8 10-8" /></svg>
          desmond@willowmereKB.example
        </li>
        <li>
          <svg viewBox="0 0 24 24" aria-hidden="true"><circle cx="12" cy="12" r="10"/><path d="M7 8c2 0 3 1 3 3s-2 2-2 4M15 5c-1 2 1 3 2 3M14 14c1 0 3 1 2 4" stroke="#fff" stroke-width="1.6" fill="none"/></svg>
          www.willowmereKB.example
        </li>
      </ul>
      <p class="contact__city">Charlotte NC</p>
    </div>

    <div class="portrait" role="img" aria-label="Portrait photo of the owner in a blazer and white shirt"></div>

    <div class="tagline">BEAUTY | FUNCTION | ON TIME | ON BUDGET</div>
  </section>
</main>
</body>
</html>
```